Brookfarrow Osteopathy and dry needling business card

Business card for Brookfarrow Osteopathy and Dry Needling.

Industry/Entity Type

Health

Contact Information for Business Card

I do not have a phone number yet. I also do not have an email address yet. The physical address is: 48 Lower Crane Street Brookfarrow The website is: www.brookfarrowosteosteopathy.example My details are: Dr Martin Pellowe, Osteopath (B.Clin.Sci (Ost) M.Ost BSC ECON (Hons)

Colors
0094D4
00A9DD
6FCCEA
C7EBF8
E9F6FB

Requirements
Must have
• logo on the back
Nice to have
• Maybe a space for me to write an appointment time and date on the card.

```html
<!DOCTYPE html>
<html lang="en">
<head>
<meta charset="utf-8">
<title>Brookfarrow Osteopathy and Dry Needling – Business Card</title>
<link href="https://fonts.googleapis.com/css2?family=Arimo:wght@400;600;700&family=Poppins:wght@700&display=swap" rel="stylesheet">
<style>
  :root {
    --blue: #0094d4;
    --blue-mid: #00a9dd;
    --orange: #f7931e;
    --ink-line: #333333;
    --white: #ffffff;
    --stage-dark: #0a0a0a;
    --stage-light: #2a2a2a;
    --grey-light: #dcdcdc;
    --grey-dark: #b2afaf;
  }
  * { margin: 0; padding: 0; box-sizing: border-box; }
  html, body { width: 1200px; height: 1000px; overflow: hidden; }
  body {
    position: relative;
    background: radial-gradient(ellipse at center, var(--stage-light) 0%, var(--stage-dark) 75%);
    font-family: "Arimo", Arial, sans-serif;
  }
  .card {
    position: absolute;
    left: 193px;
    width: 814px;
    height: 465px;
    border-radius: 22px;
    overflow: hidden;
  }
  .card-back {
    top: 25px;
    background: radial-gradient(ellipse at 50% 45%, var(--grey-light) 0%, var(--grey-dark) 85%);
  }
  .card-front { top: 509px; background: var(--white); }

  .brand-mark {
    position: absolute;
    border: 2px solid var(--blue);
    border-radius: 50%;
    display: flex;
    align-items: center;
    justify-content: center;
    text-align: center;
    color: var(--blue);
    font-weight: 700;
    text-transform: uppercase;
    line-height: 1.25;
  }
  .card-back .brand-mark {
    left: 286px; top: 112px; width: 242px; height: 242px;
    font-size: 19px; padding: 30px;
  }
  .card-front .brand-mark {
    left: 28px; top: 36px; width: 170px; height: 170px;
    font-size: 14px; padding: 20px;
  }

  .contact {
    position: absolute;
    right: 27px;
    text-align: right;
    color: var(--blue);
  }
  .website { top: 32px; font-size: 20px; display: flex; align-items: center; gap: 6px; }
  .doctor-name { top: 80px; font-size: 30px; font-weight: 700; letter-spacing: 0.3px; }
  .credentials { top: 118px; font-size: 20px; font-weight: 600; line-height: 31px; }
  .credentials .accent { color: var(--orange); }
  .address { top: 194px; font-size: 17px; display: flex; align-items: center; gap: 6px; }

  .appointment-title {
    position: absolute; left: 26px; top: 254px;
    display: flex; align-items: center; gap: 12px;
    font-family: "Poppins", Arial, sans-serif;
    font-size: 29px; font-weight: 700; color: var(--blue);
  }
  .appointment-row {
    position: absolute; top: 314px;
    font-size: 20px; color: var(--blue);
    display: flex; align-items: flex-end;
  }
  .appointment-row .blank {
    display: inline-block; height: 1px; background: var(--ink-line);
    margin-left: 6px; margin-bottom: 4px;
  }
  .row-date { left: 26px; }
  .row-date .blank { width: 286px; }
  .row-time { left: 416px; }
  .row-time .blank { width: 180px; margin-right: 16px; }

  .notice-band {
    position: absolute; left: 0; bottom: 0; width: 100%; height: 87px;
    background: var(--blue);
    color: var(--white);
    text-align: center;
    text-transform: uppercase;
    font-weight: 700;
    padding-top: 16px;
  }
  .notice-band .line-small { font-size: 17px; }
  .notice-band .line-large { font-size: 26px; margin-top: 2px; }
</style>
</head>
<body>
  <section class="card card-back" aria-label="Card back">
    <div class="brand-mark">Brookfarrow Osteopathy and Dry Needling</div>
  </section>

  <section class="card card-front" aria-label="Card front">
    <div class="brand-mark">Brookfarrow Osteopathy and Dry Needling</div>

    <div class="contact website">
      <svg width="16" height="16" viewBox="0 0 16 16" aria-hidden="true">
        <circle cx="8" cy="8" r="7" fill="var(--orange)"/>
        <path d="M1 8h14M8 1c-3 3-3 11 0 14M8 1c3 3 3 11 0 14" stroke="#fff" stroke-width="1.2" fill="none"/>
      </svg>
      www.brookfarrowosteosteopathy.example
    </div>
    <div class="contact doctor-name">DR. MARTIN PELLOWE</div>
    <div class="contact credentials">
      Osteopath (B.Clin.Sci <span class="accent">(Ost)</span><br>
      M.Ost BSC ECON <span class="accent">(Hons)</span>
    </div>
    <div class="contact address">
      48 Lower Crane Street Brookfarrow
      <svg width="14" height="19" viewBox="0 0 14 19" aria-hidden="true">
        <path d="M7 0C3 0 0 3 0 7c0 5 7 12 7 12s7-7 7-12c0-4-3-7-7-7z" fill="var(--orange)"/>
        <circle cx="7" cy="7" r="2.7" fill="#fff"/>
      </svg>
    </div>

    <div class="appointment-title">
      <svg width="38" height="40" viewBox="0 0 38 40" aria-hidden="true">
        <rect x="2" y="6" width="34" height="32" rx="4" fill="var(--blue)"/>
        <rect x="6" y="15" width="26" height="19" rx="2" fill="#fff"/>
        <rect x="9" y="1" width="4" height="10" rx="2" fill="var(--blue)"/>
        <rect x="25" y="1" width="4" height="10" rx="2" fill="var(--blue)"/>
        <path d="M11 24l5 5 10-10" stroke="var(--blue)" stroke-width="3" fill="none"/>
      </svg>
      Appointment
    </div>
    <div class="appointment-row row-date">Date :<span class="blank"></span></div>
    <div class="appointment-row row-time">Time :<span class="blank"></span>A.M. / P.M.</div>

    <div class="notice-band">
      <div class="line-small">If your unable to keep your appointment,</div>
      <div class="line-large">Kindly give us 24 hour notice</div>
    </div>
  </section>
</body>
</html>
```